Road Sign at our office 84 in X 48 in - Small Billboard

Kestrel Electrical
Electrical & Lighting Services

- we need a sign design for our small business/company based in Calhoun, GA called Kestrel Electrical - "our mission is to provide Northwest Georgia with dependable, high-quality electrical services that prioritize safety, integrity, and long-term reliability. As a woman-owned business with over 25 years of experience, we are committed to delivering exceptional workmanship and personalized service for every commercial, residential, and industrial project we undertake. We stand behind our work with a lifetime warranty—because your trust is our most powerful connection."

display logo, phone number, and open to other ideas without being cluttered, maybe instead of full website address, just use @kstelectrical and it will send them to all of our website and socials...

it needs to be easy to read as they drive down the road
this is a place where people may be traveling at high speeds, make sure it's easy to see and understand at a glance.
It will be hanging 20-24ft from the ground. Like a small billboard.

https://kstelectricalservices.example/

Industry/Entity Type

Electrical Contractor

Requirements
Nice to have
• match the look and feel of website and socials

```html
<!DOCTYPE html>
<html lang="en">
<head>
<meta charset="utf-8">
<title>Kestrel Electrical – Road Sign</title>
<link href="https://fonts.googleapis.com/css2?family=Montserrat:wght@600;700;800&display=swap" rel="stylesheet">
<style>
  :root {
    --page-bg: #4d4d4d;
    --sign-white: #ffffff;
    --brand-orange: #f26a0f;
    --ink: #111111;
    --charcoal: #2b2b2b;
    --photo-dark: #3a3532;
    --photo-mid: #6e6660;
    --photo-warm: #c9892f;
  }
  html, body {
    margin: 0;
    width: 925px;
    height: 1200px;
    overflow: hidden;
    background: var(--page-bg);
  }
  .road-sign {
    position: absolute;
    left: 0;
    top: 337px;
    width: 925px;
    height: 526px;
    display: block;
    box-shadow: 0 18px 30px rgba(0,0,0,.35);
  }
  .sign-text { font-family: "Montserrat", sans-serif; }
  .brand-name { font-weight: 700; fill: var(--charcoal); }
  .brand-name--sub { letter-spacing: 9px; }
  .years { font-weight: 800; fill: var(--brand-orange); }
  .experience { font-weight: 800; fill: var(--ink); letter-spacing: 3px; }
  .services { font-weight: 800; fill: var(--sign-white); }
  .sector { font-weight: 800; }
  .sector--orange { fill: var(--brand-orange); }
  .sector--dark { fill: var(--charcoal); }
  .contact { font-weight: 700; fill: var(--sign-white); }
</style>
</head>
<body>
<svg class="road-sign" viewBox="0 0 1364 776" xmlns="http://www.w3.org/2000/svg">
  <defs>
    <linearGradient id="panelPhotoTone" x1="0" y1="0" x2="1" y2="1">
      <stop offset="0" stop-color="var(--photo-warm)"/>
      <stop offset="0.35" stop-color="var(--photo-mid)"/>
      <stop offset="1" stop-color="var(--photo-dark)"/>
    </linearGradient>
    <linearGradient id="handPhotoTone" x1="0" y1="0" x2="1" y2="0">
      <stop offset="0" stop-color="#7d7a78"/>
      <stop offset="1" stop-color="#d9d6e0"/>
    </linearGradient>
  </defs>

  <rect class="sign-base" width="1364" height="776" fill="var(--sign-white)"/>

  <g role="img" aria-label="Photo of a gloved electrician testing wiring in an electrical control panel">
    <polygon class="panel-photo" points="585,0 1364,0 1364,776 700,776" fill="url(#panelPhotoTone)"/>
    <polygon class="hand-photo" points="530,389 865,389 1040,623 680,623" fill="url(#handPhotoTone)"/>
  </g>

  <polygon class="header-panel" points="0,0 587,0 772,277 0,277" fill="var(--sign-white)"/>
  <polygon class="years-plate" points="587,91 900,91 992,222 640,222" fill="var(--sign-white)"/>
  <polygon class="services-gap" points="0,372 850,372 862,389 0,389" fill="var(--sign-white)"/>
  <polygon class="sectors-panel" points="0,389 530,389 680,623 0,623" fill="var(--sign-white)"/>
  <polygon class="white-stripe" points="844,372 872,372 1048,608 1020,608" fill="var(--sign-white)"/>
  <polygon class="white-stripe" points="0,608 1040,608 1052,623 0,623" fill="var(--sign-white)"/>
  <polygon class="white-stripe" points="940,0 972,0 1220,300 1190,300" fill="var(--sign-white)"/>
  <polygon class="white-stripe" points="987,478 1012,478 1262,776 1236,776" fill="var(--sign-white)"/>
  <polygon class="white-stripe" points="1060,623 1082,623 1200,776 1178,776" fill="var(--sign-white)"/>

  <polygon class="orange-slash" points="520,92 560,92 650,222 610,222" fill="var(--brand-orange)"/>
  <polygon class="orange-stripe" points="856,0 890,0 1012,165 978,165" fill="var(--brand-orange)"/>
  <polygon class="orange-stripe" points="1176,612 1198,612 1330,776 1306,776" fill="var(--brand-orange)"/>
  <polygon class="services-band" points="0,277 772,277 844,372 0,372" fill="var(--brand-orange)"/>

  <polygon class="contact-bar" points="0,623 1042,623 1157,776 0,776" fill="var(--ink)"/>

  <!-- brand -->
  <circle class="brand-dot" cx="104" cy="142" r="46" fill="var(--brand-orange)"/>
  <text class="sign-text brand-name" x="178" y="160" font-size="70">Kestrel</text>
  <text class="sign-text brand-name brand-name--sub" x="182" y="206" font-size="28">ELECTRICAL</text>

  <text class="sign-text years" x="620" y="153" font-size="48">25+ YEARS</text>
  <text class="sign-text experience" x="652" y="196" font-size="35">EXPERIENCE</text>

  <text class="sign-text services" x="50" y="341" font-size="38.5">ELECTRICAL &amp; LIGHTING SERVICES</text>

  <rect class="bullet" x="50" y="424" width="30" height="30" fill="var(--ink)"/>
  <text class="sign-text sector sector--orange" x="107" y="458" font-size="56">COMMERCIAL</text>
  <rect class="bullet" x="112" y="487" width="30" height="30" fill="var(--ink)"/>
  <text class="sign-text sector sector--dark" x="168" y="520" font-size="56">RESIDENTIAL</text>
  <rect class="bullet" x="212" y="551" width="30" height="30" fill="var(--ink)"/>
  <text class="sign-text sector sector--orange" x="267" y="585" font-size="56">INDUSTRIAL</text>

  <!-- phone -->
  <g transform="translate(16,210) scale(0.7)">
    <path class="phone-icon" d="M52,686 c4,-3 8,-3 10,1 l6,9 c2,3 1,6 -2,8 l-3,2 c2,6 6,11 12,14 l2,-3 c2,-3 5,-4 8,-2 l8,6 c3,2 3,6 0,9 l-4,4 c-6,5 -20,0 -30,-11 c-10,-11 -14,-24 -9,-30 z" fill="var(--brand-orange)"/>
  </g>
  <text class="sign-text contact" x="94" y="722" font-size="54">706-555-0148</text>
  <rect class="divider" x="541" y="665" width="4" height="74" fill="var(--sign-white)"/>

  <circle class="handle-dot" cx="602" cy="701" r="20" fill="none" stroke="var(--brand-orange)" stroke-width="6"/>
  <text class="sign-text contact" x="640" y="718" font-size="56">kstelectrical</text>
</svg>
</body>
</html>
```